Heading: Tarraway (small font: under Tarraway.. LIVE IN NOOSA)

We need a flyer for an upcoming Live show. (Double sided DL)
It is a magic & comedy show . We would like it to feel like its a high end classy show as it will be at a 5 star hotel. We like the look of all the Théâtre des Ombres posters (maybe google to have a look - I have attached some examples of what we like.
INFO FOR FLYER DOUBLE SIDED DL FLYER
Promo Photo- FOR FRONT OF FLYER : https://www.filedrop-example.com/s/kq7trzp2mwx/Lorne%20Baxter%20Studio%20%28358%20of%20530%29.jpg?dl=0
A world-class experience combining comedy, magic and illusion.
Tarraway has Performed live to over 1 million people.
*****
“HIGHLY ENTERTAINING (add 5 star graphics)
SENSATIONAL SHOW”
Marla Quintrell
*****
"TARRAWAY’S SHOW WAS BETTER THAN HARGROVE IN VEGAS. LOVED IT!”
Jocelyn & Warren Pitcairn
*****
“BEST MAGIC SHOW I’VE SEEN…
HAD US IN STITCHES LAUGHING THE WHOLE TIME”
Pepita Lou
SESSION ONE
FAMILY SHOW 5:30PM $38 PP
SESSION TWO
LATE SESSION 8PM $49.00 PP
NOOSA DATES
Thursday 24th Sept
Saturday 26th Sept
Thursday 1st October
Saturday 3rd October
BOOK ONLINE NOW - www.tarraway.com.au
BRAMBLEWOOD RESORT NOOSA LOGO (NEAR THE BOTTOM)
BACK OF FLYER
Add dinner to your award-winning show experience.
Supper at Ridge by Owen Trevallick (ADD LOGO)
Two courses including a glass of wine $39.00
Two sittings, 6.30pm and 7pm.
Tables limited, so please book early to secure your table.
Booking details via Tarraway.com.au
Ridge Bar
Open from 12pm daily.
BRAMBLEWOOD Resort LOGO
Only a 5 minute stroll from Corrigan Street, Noosa Heads
Vehicle Entry/Exit
Vehicle entry/exit as follows:
Tallowood Drive (7pm-7am, Little Corrigan Street),
Kestrelbank Drive (7am-7pm, Orla Way).
(please add map)
On-Site Parking
Limited parking is available on-site. Once parking is full, guests will be directed to park on Kestrelbank Drive, with the resort buggy service available to transport guests up/down the driveway.
Covid Safety, Contact Tracing & distancing regulations are in place.
More Info: www.tarraway.com.au

```html
<!DOCTYPE html>
<html lang="en">
<head>
<meta charset="utf-8">
<title>Tarraway – Live in Noosa</title>
<link rel="stylesheet" href="https://fonts.googleapis.com/css2?family=Montserrat:ital,wght@0,600;0,800;0,900;1,500&family=Kanit:ital,wght@1,500&family=Tinos:wght@400;700&display=swap">
<style>
  :root {
    --paper: #ffffff;
    --navy-deep: #1b1f63;
    --navy: #2a3590;
    --violet-glow: #8f8fd6;
    --haze: #c9c7ef;
    --gold: #f1ea2a;
    --white: #ffffff;
    --shadow: #0d0f2e;
  }
  * { margin: 0; padding: 0; box-sizing: border-box; }
  html, body { width: 1200px; height: 2469px; overflow: hidden; background: var(--paper); }
  .flyer { position: relative; width: 1200px; height: 2469px; background: var(--paper); }
  .panel {
    position: absolute; left: 45px; top: 45px; width: 1105px; height: 2368px; overflow: hidden;
    background:
      radial-gradient(ellipse 520px 620px at 560px 360px, rgba(201,199,239,.85), rgba(143,143,214,.35) 55%, transparent 80%),
      radial-gradient(ellipse 620px 260px at 560px 1060px, rgba(90,110,220,.55), transparent 70%),
      radial-gradient(ellipse 500px 420px at 560px 1960px, rgba(50,75,180,.55), transparent 75%),
      linear-gradient(180deg, #4a4fa8 0%, var(--navy) 30%, var(--navy-deep) 60%, var(--navy) 100%);
  }
  .hero-art {
    position: absolute; left: 160px; top: 80px; width: 870px; height: 900px;
    background:
      radial-gradient(ellipse 170px 380px at 430px 470px, rgba(20,20,40,.9) 0%, rgba(26,27,51,.6) 60%, transparent 100%),
      radial-gradient(ellipse 430px 220px at 430px 650px, rgba(255,232,140,.35), transparent 75%),
      radial-gradient(ellipse 430px 400px at 430px 330px, rgba(220,220,245,.45), transparent 80%);
  }
  .text-block { position: absolute; left: 0; width: 1105px; text-align: center; }
  .title {
    top: 820px; font-family: "Montserrat", sans-serif; font-weight: 900; font-size: 214px;
    color: var(--white); letter-spacing: -10px; line-height: 1;
    text-shadow: -6px 8px 0 var(--shadow);
  }
  .title-flare {
    position: absolute; left: 120px; top: 1005px; width: 880px; height: 30px;
    background: radial-gradient(ellipse at center, rgba(200,225,255,.9), rgba(120,160,255,.35) 40%, transparent 72%);
  }
  .subtitle {
    top: 1051px; font-family: "Tinos", serif; font-weight: 700; font-size: 54px; line-height: 62px;
    color: var(--gold); text-shadow: 2px 3px 0 var(--shadow); letter-spacing: -1px;
  }
  .tagline {
    top: 1125px; font-family: "Kanit", sans-serif; font-style: italic; font-weight: 500;
    font-size: 33px; line-height: 43px; color: var(--white); letter-spacing: .5px;
    text-shadow: 1px 2px 2px rgba(0,0,0,.5);
  }
  .stars { display: block; font-family: "Montserrat", sans-serif; font-weight: 800; font-size: 30px; line-height: 30px; height: 30px; color: var(--gold); letter-spacing: 2px; }
  .quote {
    font-family: "Montserrat", sans-serif; font-weight: 600; font-size: 32px; line-height: 39px;
    color: var(--gold); letter-spacing: -1px; text-shadow: 1px 2px 2px rgba(0,0,0,.45);
  }
  .quote .star-row { letter-spacing: 0; }
  .reviewer {
    font-family: "Montserrat", sans-serif; font-style: italic; font-weight: 500; font-size: 23px; line-height: 28px;
    color: var(--white); margin-top: 5px; letter-spacing: -.5px;
  }
  .review { display: flex; flex-direction: column; align-items: center; }
  .review .stars { margin-bottom: 23px; }
  .review--one { top: 1231px; }
  .review--two { top: 1419px; }
  .review--three { top: 1608px; }
  .session { position: absolute; width: 420px; text-align: center; top: 1813px; font-family: "Tinos", serif; }
  .session--one { left: 67px; }
  .session--two { left: 619px; }
  .session__label {
    display: inline-block; font-size: 38px; color: var(--white); letter-spacing: -1.5px;
    border-top: 3px solid var(--white); border-bottom: 3px solid var(--white); padding: 0 2px; line-height: 46px;
  }
  .session__time { font-size: 34px; color: var(--white); letter-spacing: -1.5px; margin-top: 12px; line-height: 40px; }
  .session__price { font-size: 34px; font-weight: 700; color: var(--gold); letter-spacing: -1px; line-height: 40px; }
  .dates { top: 1970px; font-family: "Montserrat", sans-serif; font-style: italic; color: var(--white); }
  .dates__heading { font-family: "Kanit", sans-serif; font-size: 35px; color: var(--gold); word-spacing: 8px; line-height: 42px; }
  .dates__list { list-style: none; font-size: 27px; line-height: 34px; font-weight: 500; letter-spacing: -1px; }
  .booking { top: 2181px; font-family: "Tinos", serif; font-size: 32px; line-height: 40px; color: var(--white); letter-spacing: -1.5px; }
  .venue-mark {
    position: absolute; left: 454px; top: 2243px; width: 206px; height: 100px; background: var(--white);
    display: flex; align-items: center; justify-content: center;
    font-family: "Montserrat", sans-serif; font-weight: 600; font-size: 19px; color: var(--navy-deep); letter-spacing: 1px;
  }
</style>
</head>
<body>
<div class="flyer">
  <section class="panel">
    <div class="hero-art" role="img" aria-label="Promo photo of the magician in a black suit, surrounded by a fanned deck of cards, a hand holding a wand, a white rabbit, doves and glowing golden light rings"></div>

    <h1 class="text-block title">Tarraway</h1>
    <div class="title-flare"></div>
    <p class="text-block subtitle">LIVE IN NOOSA</p>
    <p class="text-block tagline">A world-class experience combining comedy, magic and illusion.<br>Tarraway has Performed live to over 1 million people.</p>

    <div class="text-block review review--one">
      <span class="stars">*****</span>
      <p class="quote">“HIGHLY ENTERTAINING <span class="star-row">★★★★★</span><br>SENSATIONAL SHOW”</p>
      <p class="reviewer">Marla Quintrell</p>
    </div>
    <div class="text-block review review--two">
      <span class="stars">*****</span>
      <p class="quote">"TARRAWAY’S SHOW WAS BETTER THAN<br>HARGROVE IN VEGAS. LOVED IT!”</p>
      <p class="reviewer">Jocelyn &amp; Warren Pitcairn</p>
    </div>
    <div class="text-block review review--three">
      <span class="stars">*****</span>
      <p class="quote">“BEST MAGIC SHOW I’VE SEEN…<br>HAD US IN STITCHES LAUGHING THE WHOLE TIME”</p>
      <p class="reviewer">Pepita Lou</p>
    </div>

    <div class="session session--one">
      <span class="session__label">SESSION ONE</span>
      <p class="session__time">FAMILY SHOW 5:30PM</p>
      <p class="session__price">$38 PP</p>
    </div>
    <div class="session session--two">
      <span class="session__label">SESSION TWO</span>
      <p class="session__time">LATE SESSION 8PM</p>
      <p class="session__price">$49.00 PP</p>
    </div>

    <div class="text-block dates">
      <p class="dates__heading">– NOOSA DATES –</p>
      <ul class="dates__list">
        <li>Thursday 24th Sept</li>
        <li>Saturday 26th Sept</li>
        <li>Thursday 1st October</li>
        <li>Saturday 3rd October</li>
      </ul>
    </div>

    <p class="text-block booking">BOOK ONLINE NOW - www.tarraway.com.au</p>

    <div class="venue-mark">BRAMBLEWOOD</div>
  </section>
</div>
</body>
</html>
```